Timeline flyer

Hi, we are an agency, our business is to orienteates student to study abroad in Germany. For that, we enroll them in language schools in Germany and help them to find an accomodation.
Students are always lost we thinked about a timeline to help them figure out what they have to do once in Germany so they don't miss delays.
You can find in the attachement an example that i made in powerpoint but it's really basic and it's only for u so you can understant what the timeline should look like.
We need two time lines.
For the first one (file first timeline)
Title : Procédure pour intégrer le semestre d’hiver dans les universités Allemandes
The first paragraph (up on the left in my proposition) : L’étudiant devra pendant ces mois débuter ses cours d’allemand en Tunisie et les poursuivre en Allemagne après l’obtention du Visa d’étude. L’atteinte du niveau C1 est primordiale pour la bonne réussite du test Kel ou le MRT.
The second paragraph (below on the left in my proposition) : L’étudiant devra à cette date avoir déjà passer le test KEL ou le MRT pour pouvoir être à temps pour les inscriptions universitaires. Il faut compter 6 semaines pour le test Kel et 2 à 3 semaines pour obtenir les résultats des tests.
The third one (up on the right in my proposition) : Le dernier délais d’inscription pour pouvoir intégrer une université Allemande pendant la rentrée hivernale (15 Octobre).
The last one (below on the right in my proposition) : Rentrée universitaire
For the second one (file second timeline) :
Title : Procédure pour intégrer le semestre d’été dans les universités Allemandes *
The third one (up on the right in my proposition) : Le dernier délais d’inscription pour pouvoir intégrer une université Allemande pendant la rentrée estivale (15 Avril).
There is also an additional sentence below in the right for this one : * Les spécialités assurées pendant les semestres d’été sont limitées.
You can also find in the attachement our flyers (so you can inspire youself with the color and the design), we want our student to recognize that the flyer is related to our agency so please try to use colors that are matched with the other flyer.
Also, you can find our Logo in the attachement.
Thank you :)
Waiting for your propositions ! :)

```html
<!DOCTYPE html>
<html lang="fr">
<head>
<meta charset="utf-8">
<title>Semestre d'hiver – Lernweg</title>
<link rel="stylesheet" href="https://fonts.googleapis.com/css2?family=Montserrat:wght@300;400;600;700&family=Oswald:wght@300;400&family=Lato:wght@400;700&display=swap">
<style>
  :root{
    --teal:#1f8b90;
    --teal-dark:#136267;
    --teal-light:#36a9ad;
    --yellow:#d9dd1c;
    --ink:#3f4446;
    --paper:#f3f4f4;
    --paper-shade:#dde2e2;
  }
  *{margin:0;padding:0;box-sizing:border-box}
  html,body{width:1027px;height:1200px;overflow:hidden;background:#e9ebeb}
  .flyer{position:relative;width:1027px;height:1200px;overflow:hidden;
    background:linear-gradient(180deg,var(--paper) 0%,#ffffff 45%,var(--paper-shade) 100%);
    font-family:'Lato',sans-serif;color:var(--ink)}
  .header-panel{position:absolute;left:0;top:0;width:412px;height:400px;
    background:radial-gradient(circle at 35% 40%,var(--teal-light) 0%,var(--teal) 45%,var(--teal-dark) 100%)}
  .header-divider{position:absolute;left:412px;top:0;width:14px;height:400px;background:var(--yellow)}
  .header-photo{position:absolute;left:426px;top:0;width:601px;height:400px;
    background:linear-gradient(135deg,#8a6a4c 0%,#c9b8a0 40%,#d86a6e 70%,#4a7fb8 100%)}
  .header-curve{position:absolute;left:0;top:0;width:1027px;height:440px}
  .brand{position:absolute;left:95px;top:170px;display:flex;align-items:center;gap:14px}
  .brand-dot{width:26px;height:26px;border-radius:50%;background:var(--yellow)}
  .brand-name{font-family:'Montserrat',sans-serif;font-weight:700;font-size:52px;color:var(--yellow);letter-spacing:-1px}
  .title{position:absolute;left:0;top:448px;width:100%;text-align:center}
  .title-lead{font-family:'Montserrat',sans-serif;font-weight:400;font-size:42px;color:var(--ink)}
  .title-main{font-family:'Oswald',sans-serif;font-weight:300;font-size:46px;line-height:1.15;color:var(--teal)}
  .steps{position:absolute;left:150px;top:615px;display:flex;gap:14px}
  .step{width:368px;height:210px;background:var(--yellow);border:4px solid var(--teal);border-radius:16px;
    padding:22px 24px;font-size:17px;line-height:1.4;text-align:justify;color:var(--ink);
    box-shadow:0 6px 10px rgba(0,0,0,.25)}
  .deadline{position:absolute;left:190px;top:855px;width:680px;font-size:18px;line-height:1.35;color:var(--ink)}
  .start{position:absolute;left:300px;top:925px;width:430px;height:78px;border:5px solid var(--yellow);border-radius:22px;
    background:linear-gradient(180deg,var(--teal-light),var(--teal-dark));
    display:flex;align-items:center;justify-content:center;color:#fff;font-family:'Montserrat',sans-serif;font-size:38px;
    box-shadow:0 5px 8px rgba(0,0,0,.25)}
  .start b{font-weight:700;margin-left:10px}
  .start span{font-weight:300}
  .contacts{position:absolute;left:0;top:1030px;width:100%;text-align:center;font-family:'Montserrat',sans-serif;
    font-weight:700;font-size:24px;letter-spacing:2px;line-height:1.4;color:var(--teal)}
  .footer{position:absolute;left:0;bottom:0;width:100%;height:92px;
    background:linear-gradient(90deg,var(--teal-dark),var(--teal-light) 50%,var(--teal-dark));
    border-top:3px solid var(--yellow);
    display:flex;align-items:center;justify-content:center;color:#fff;font-family:'Montserrat',sans-serif;font-size:24px;letter-spacing:10px}
</style>
</head>
<body>
<main class="flyer">
  <div class="header-panel"></div>
  <div class="header-divider"></div>
  <div class="header-photo" role="img" aria-label="Photo d'un groupe d'étudiants travaillant ensemble dans une bibliothèque"></div>
  <svg class="header-curve" viewBox="0 0 1027 440" aria-hidden="true">
    <path d="M0,362 Q540,250 1027,350 L1027,372 Q540,275 0,388 Z" fill="var(--yellow)"/>
    <path d="M0,388 Q540,275 1027,372 L1027,386 Q540,292 0,402 Z" fill="var(--teal-dark)"/>
    <path d="M0,402 Q540,292 1027,386 L1027,440 L0,440 Z" fill="var(--paper)"/>
  </svg>
  <div class="brand">
    <span class="brand-dot"></span>
    <span class="brand-name">lernweg</span>
  </div>

  <header class="title">
    <p class="title-lead">Procédure pour intégrer</p>
    <h1 class="title-main">le semestre d’hiver dans les universités<br>Allemandes</h1>
  </header>

  <section class="steps">
    <p class="step">L’étudiant devra pendant ces mois débuter ses cours d’allemand en Tunisie et les poursuivre en Allemagne après l’obtention du Visa d’étude. L’atteinte du niveau C1 est primordiale pour la bonne réussite du test Kel ou le MRT.</p>
    <p class="step">L’étudiant devra à cette date avoir déjà passer le test KEL ou le MRT pour pouvoir être à temps pour les inscriptions universitaires. Il faut compter 6 semaines pour le test Kel et 2 à 3 semaines pour obtenir les résultats des tests.</p>
  </section>

  <p class="deadline">Le dernier délais d’inscription pour pouvoir intégrer une université Allemande pendant la rentrée hivernale (15 Octobre).</p>

  <div class="start"><span>Rentrée</span><b>universitaire</b></div>

  <address class="contacts" style="font-style:normal">
    LERNWEG / TÉL. : 70 123 456<br>
    SFAX : 74 000 111 / SOUSSE : 58 000 222
  </address>

  <footer class="footer">www.lernweg.org</footer>
</main>
</body>
</html>
```